Dane Moro films- wedding and event films company website. DESKTOP AND MOBILE

We need a website for a high-end wedding and event film production company. Looking for a very modern and elegant design. my old website is www.danemorofilms.example

I like the "white/black/rose gold" color scheme of my logo.

really looking for a sleek modern design the breaths professional and artistic.

Target Market(s)

wedding and event films.

Industry/Entity Type

Film Production

Number of Pages Required

5+ page

Colors

Designer to choose colors to be used in the design.

Requirements
Must have
• website name will be www.danemorofilms.example
• tagline is "CINEMATIC STORIES ABOUT YOU"
• sections: HOME, CONTACT, ABOUT, FILMS, BLOG
• You can see my old website at danemorofilms.example
• Website about section:
• Dane Moro Films was Established with the basis of truly cinematic and artistic films in mind. Dane and his team routinely travel the globe documenting weddings and events for high profile clients and discerning couples. Dane was born and raised in Maui Hawaii and has a unique approach to his films that embody the essence of a Hollywood film. Dane has spent the last 10 years traveling the world documenting corporate events and weddings with multiple Award winning production companies. In 2017 Dane decided to establish his own brand “Dane Moro films” that will take everything he has learned with his past experiences and push it to the next level. Aside from his personal achievements, Dane is extremely passionate about his craft and always looks forward to handcrafting beautiful wedding/event films for his clients. The style of work is non-traditional and the day of filming is extremely unobtrusive (as we are looking for natural-candid/ raw emotions).
• If you are looking for the best price in town, we are probably not the best option, but if you’re looking for the best quality and peace of mind on your wedding day, then you’re in the right place. Dane Moro Films is a boutique studio that only accepts a limited number of assignments per year. Inquire early to ensure availability.
• LINKS TO VIMEO VIDEOS THAT WILL BE IN THE "FILMS' SECTION.
• BRENT FILM TRAILER - https://clipvault.example/418205736
• BRENT FEATURE FILM - https://clipvault.example/527910384
• NORA AND PAUL'S WEDDING - https://clipvault.example/649382015
• DRONE DEMO REEL - https://clipvault.example/751046923
• WEDDING INDUSTRY EVENT PARTY - https://clipvault.example/862937104/7a2d9c3e8b
• images that you can use on site are here: https://maribelortegaphotos.picvault.example/gallery/ruth&glen/
• password is: meadow

```html
<!DOCTYPE html>
<html lang="en">
<head>
<meta charset="utf-8">
<title>Dane Moro Films</title>
<link rel="stylesheet" href="https://fonts.googleapis.com/css2?family=Montserrat:wght@300;400;500&display=swap">
<style>
:root{
  --copper:#b9794c;
  --copper-line:#d4a687;
  --ink:#1c1c1c;
  --muted:#444;
  --paper:#ffffff;
  --field-line:#555;
}
*{box-sizing:border-box;margin:0;padding:0}
html,body{width:1200px;height:3197px;overflow:hidden;background:var(--paper)}
body{position:relative;font-family:'Montserrat',sans-serif;color:var(--ink)}
.abs{position:absolute}

.hero{left:0;top:0;width:1200px;height:697px;background:linear-gradient(180deg,#7d7d7d 0%,#d9d9d9 30%,#9a9a9a 65%,#4a4a4a 100%)}
.brand-tab{left:132px;top:0;width:205px;height:309px}
.brand-tab svg{position:absolute;left:0;top:0}
.brand-name{position:absolute;left:0;top:78px;width:205px;text-align:center;font-size:17px;font-weight:500;letter-spacing:2px;color:var(--muted)}
.brand-dot{display:inline-block;width:8px;height:8px;background:var(--copper);margin-right:6px;vertical-align:2px}
.main-nav{position:absolute;left:0;top:141px;width:205px;list-style:none;text-align:center}
.main-nav li{font-size:10.5px;letter-spacing:.8px;color:var(--ink);height:24px;line-height:24px}

.portrait{left:145px;top:778px;width:413px;height:411px;background:linear-gradient(135deg,#d8d8d8,#8a8a8a 55%,#2b2b2b)}
.kicker{font-size:13px;font-weight:500;letter-spacing:1px;color:var(--ink)}
.heading{font-size:24px;font-weight:400;letter-spacing:1px;color:var(--copper)}
.rule{height:1px;background:var(--copper-line)}
.about-kicker{left:614px;top:807px}
.about-heading{left:614px;top:822px}
.about-rule{left:511px;top:867px;width:388px}
.about-copy{left:614px;top:894px;width:441px;font-size:12.4px;line-height:20.4px;color:var(--ink)}

.film{left:145px;top:1272px;width:910px;height:461px;background:radial-gradient(circle at 80% 30%,#e8e8e8,#7a7a7a 45%,#2e2e2e)}
.play{left:554px;top:1470px;width:98px;height:64px}

.services-kicker{left:143px;top:1770px}
.services-heading{left:143px;top:1786px}
.services-rule{left:0;top:1828px;width:352px}
.service{width:180px;text-align:center;top:1775px}
.service svg{display:block;margin:0 auto}
.service span{display:block;margin-top:14px;font-size:12.5px;letter-spacing:.8px;color:var(--copper)}

.blogs-kicker{right:147px;top:1966px;text-align:right}
.blogs-heading{right:147px;top:1981px;text-align:right}
.blogs-rule{left:846px;top:2022px;width:354px}
.post{top:2073px;width:443px}
.post-image{height:299px}
.post-date{margin-top:19px;text-align:center;font-size:11px;letter-spacing:.8px}
.post-rule{width:72px;height:1px;background:var(--copper-line);margin:8px auto 0}
.post-excerpt{margin-top:16px;text-align:center;font-size:11.6px;line-height:19px;letter-spacing:.6px;color:var(--ink)}

.msg-kicker{left:0;width:1200px;top:2582px;text-align:center}
.msg-heading{left:0;width:1200px;top:2596px;text-align:center}
.msg-rule{left:422px;top:2640px;width:354px}
.field-label{font-size:11px;letter-spacing:.8px;color:var(--ink)}
.field-line{height:2px;background:var(--field-line)}
.textarea{left:143px;top:2885px;width:912px;height:152px;border:2px solid var(--field-line);padding:12px 14px}
.send{left:509px;top:3077px;width:181px;height:56px;border:1.5px solid var(--copper-line);color:var(--copper);font-size:14px;letter-spacing:1.2px;text-align:center;line-height:53px}
</style>
</head>
<body>

<header>
  <div class="abs hero" role="img" aria-label="Black and white photo of a bride and groom kissing under a windswept veil on a beach"></div>
  <div class="abs brand-tab">
    <svg width="205" height="309" viewBox="0 0 205 309"><polygon points="0,0 205,0 205,283 102.5,309 0,283" fill="#fff"/></svg>
    <div class="brand-name"><span class="brand-dot"></span>DANE MORO</div>
    <ul class="main-nav">
      <li>HOME</li><li>CONTACT</li><li>ABOUT</li><li>FILMS</li><li>BLOG</li>
    </ul>
  </div>
</header>

<section class="about">
  <div class="abs portrait" role="img" aria-label="Black and white portrait of the filmmaker"></div>
  <div class="abs kicker about-kicker">ABOUT</div>
  <h2 class="abs heading about-heading">DANIEL MORO</h2>
  <div class="abs rule about-rule"></div>
  <p class="abs about-copy">Dane Moro Films was Established with the basis of truly cinematic and artistic films in mind. Dane and his team routinely travel the globe documenting weddings and events for high profile clients and discerning couples. Dane was born and raised in Maui Hawaii and has a unique approach to his films that embody the essence of a Hollywood film. Dane has spent the last 10 years traveling the world documenting corporate events and weddings with multiple Award winning production companies. In 2017 Dane decided to establish his own brand “Dane Moro films” that will take everything he has learned with his past experiences and push it to the next level. Aside from his personal achievements, Dane is extremely passionate about his craft and always looks forward to handcrafting beautiful wedding/event films for his clients.</p>
</section>

<section class="showreel">
  <div class="abs film" role="img" aria-label="Black and white video still of a bride and groom dancing under string lights"></div>
  <svg class="abs play" viewBox="0 0 98 64"><rect width="98" height="64" rx="12" fill="#fff"/><polygon points="40,18 40,46 62,32" fill="var(--copper)"/></svg>
</section>

<section class="services">
  <div class="abs kicker services-kicker">OUR</div>
  <h2 class="abs heading services-heading">SERVICES</h2>
  <div class="abs rule services-rule"></div>

  <div class="abs service" style="left:394px">
    <svg width="86" height="80" viewBox="0 0 86 80" fill="none" stroke="var(--copper)" stroke-width="2.5"><circle cx="32" cy="50" r="22"/><circle cx="54" cy="50" r="22"/><path d="M36 20 l7 -8 l7 8 l-7 6z"/><path d="M43 4v4M30 8l3 3M56 8l-3 3"/></svg>
    <span>WEDDING SHOOT</span>
  </div>
  <div class="abs service" style="left:632px">
    <svg width="86" height="80" viewBox="0 0 86 80" fill="none" stroke="var(--copper)" stroke-width="2.5"><rect x="14" y="28" width="58" height="46"/><path d="M14 28 l4 -18 l56 0 l-2 18"/><path d="M28 10l-6 18M44 10l-6 18M60 10l-6 18"/><path d="M22 42h42M22 52h42M22 62h30"/></svg>
    <span>FILMING</span>
  </div>
  <div class="abs service" style="left:869px">
    <svg width="86" height="80" viewBox="0 0 86 80" fill="none" stroke="var(--copper)" stroke-width="2.5"><circle cx="32" cy="16" r="10"/><circle cx="54" cy="18" r="8"/><rect x="20" y="30" width="42" height="26"/><path d="M62 38l14 -7v24l-14 -7"/><path d="M12 40h8M41 56v8M41 64l-12 12M41 64l12 12"/></svg>
    <span>EVENT SHOOT</span>
  </div>
</section>

<section class="blog">
  <div class="abs kicker blogs-kicker">LATEST</div>
  <h2 class="abs heading blogs-heading">BLOGS</h2>
  <div class="abs rule blogs-rule"></div>

  <article class="abs post" style="left:145px">
    <div class="post-image" role="img" aria-label="Black and white photo of a wooden just married sign on a car" style="background:linear-gradient(135deg,#3a3a3a,#bdbdbd 55%,#6d6d6d)"></div>
    <div class="post-date">20.10.2017</div>
    <div class="post-rule"></div>
    <p class="post-excerpt">LOREM IPSUM DOLOR SIT AMET, CONSECTETUR ADIPISCING ELIT, SED DO EIUSMOD TEMPOR INCIDIDUNT UT LABORE ET DOLORE MAGNA ALIQUA.</p>
  </article>
  <article class="abs post" style="left:612px">
    <div class="post-image" role="img" aria-label="Black and white photo of a rose centrepiece in a bright wedding tent" style="background:linear-gradient(135deg,#7a7a7a,#e6e6e6 50%,#f6f6f6)"></div>
    <div class="post-date">20.10.2017</div>
    <div class="post-rule"></div>
    <p class="post-excerpt">LOREM IPSUM DOLOR SIT AMET, CONSECTETUR ADIPISCING ELIT, SED DO EIUSMOD TEMPOR INCIDIDUNT UT LABORE ET DOLORE MAGNA ALIQUA.</p>
  </article>
</section>

<section class="contact">
  <div class="abs kicker msg-kicker">DROP</div>
  <h2 class="abs heading msg-heading">MESSAGES</h2>
  <div class="abs rule msg-rule"></div>

  <div class="abs field-label" style="left:143px;top:2725px">NAME</div>
  <div class="abs field-line" style="left:143px;top:2761px;width:424px"></div>
  <div class="abs field-label" style="left:631px;top:2725px">E-MAIL</div>
  <div class="abs field-line" style="left:631px;top:2761px;width:424px"></div>
  <div class="abs field-label" style="left:143px;top:2806px">SUBJECT</div>
  <div class="abs field-line" style="left:143px;top:2840px;width:912px"></div>
  <div class="abs textarea"><span class="field-label">SUBJECT</span></div>
  <div class="abs send">SEND</div>
</section>

</body>
</html>
```